Billboard design for dentist that sees only children

I own a 12' x 25' digital billboard and I need help with billboard design. My wife is a general dentist that only sees children and is very passionate about giving them a quality dental experience . She has a great reputation in town. Obviously with a billboard there can't be a lot of reading. Maybe something that shows safety, love, experience and children. I am completely open to your ideas. In addition I have other businesses that also need billboard design so this could lead to more work. If you go to Maplecovedental.com under the about section you will find more information about the practice and our phone number. Attached is our logo which could be changed and content specs for the digital billboard. Happy Designing!!

Target Market(s)

Parents with children

Colors

Designer to choose colors to be used in the design.

Requirements
Must have
• Must attract attention and be nice to look at.
Nice to have
• Probably should have children in the picture ..... Maybe
Should not have
• If I see something I don't like I will let you know

```html
<!DOCTYPE html>
<html lang="en">
<head>
<meta charset="UTF-8">
<title>Maple Cove Dental — Billboard</title>
<link rel="stylesheet" href="https://fonts.googleapis.com/css2?family=Bebas+Neue&family=Open+Sans:ital,wght@0,400;1,400&display=swap">
<style>
  :root {
    --page-bg: #3a3b3d;
    --header-white: #ffffff;
    --sky-blue: #1a8fe8;
    --sky-blue-light: #3fb0ff;
    --accent-green: #0a9444;
    --brand-teal: #2d6f64;
    --tagline-blue: #3470aa;
    --headline-white: #f4f5f7;
    --skin-warm: #f0c4a4;
    --hair-ginger: #c98a55;
    --towel-blue: #4aa9dc;
  }
  html, body {
    margin: 0;
    width: 1200px;
    height: 1200px;
    overflow: hidden;
    background: var(--page-bg);
  }
  .billboard {
    position: absolute;
    left: 40px;
    top: 331px;
    width: 1120px;
    height: 538px;
    overflow: hidden;
    background: linear-gradient(90deg, var(--sky-blue) 0%, var(--sky-blue) 55%, var(--sky-blue-light) 80%, var(--sky-blue) 100%);
  }
  .header-band {
    position: absolute;
    left: 0; top: 0;
    width: 100%;
    height: 118px;
    background: var(--header-white);
  }
  .header-rule {
    position: absolute;
    left: 0; top: 116px;
    width: 100%;
    height: 5px;
    background: var(--accent-green);
  }
  .brand-mark {
    position: absolute;
    left: 90px; top: 24px;
    width: 68px; height: 68px;
    border: 4px solid var(--brand-teal);
    border-radius: 50%;
    box-sizing: border-box;
  }
  .brand-name {
    position: absolute;
    left: 178px; top: 22px;
    margin: 0;
    font-family: "Open Sans", sans-serif;
    font-weight: 400;
    font-size: 40px;
    line-height: 1;
    color: var(--brand-teal);
    white-space: nowrap;
  }
  .brand-tagline {
    position: absolute;
    left: 300px; top: 66px;
    margin: 0;
    font-family: "Open Sans", sans-serif;
    font-style: italic;
    font-size: 19px;
    line-height: 1;
    color: var(--tagline-blue);
    white-space: nowrap;
  }
  .child-photo {
    position: absolute;
    left: 672px; top: 48px;
    width: 448px; height: 490px;
    background:
      radial-gradient(ellipse 38% 30% at 48% 18%, var(--hair-ginger) 0%, rgba(201,138,85,0) 100%),
      radial-gradient(ellipse 36% 34% at 50% 42%, var(--skin-warm) 0%, rgba(240,196,164,0) 100%),
      radial-gradient(ellipse 55% 30% at 50% 95%, var(--towel-blue) 0%, rgba(74,169,220,0) 100%),
      radial-gradient(ellipse 60% 60% at 50% 45%, #8fd0ff 0%, rgba(143,208,255,0) 100%);
  }
  .headline {
    position: absolute;
    left: 0; top: 128px;
    width: 600px;
    margin: 0;
    text-align: center;
    font-family: "Bebas Neue", sans-serif;
    font-weight: 400;
    color: var(--headline-white);
    line-height: 0.78;
  }
  .headline .line-big { display: block; font-size: 158px; }
  .headline .line-small { display: block; font-size: 80px; margin-top: 10px; }
  .phone-box {
    position: absolute;
    left: 70px; top: 452px;
    width: 462px; height: 66px;
    background: var(--accent-green);
    display: flex;
    align-items: center;
    justify-content: center;
  }
  .phone-number {
    font-family: "Open Sans", sans-serif;
    font-style: italic;
    font-size: 44px;
    letter-spacing: 2px;
    color: var(--headline-white);
  }
</style>
</head>
<body>
  <section class="billboard">
    <div class="header-band"></div>
    <div class="header-rule"></div>
    <div class="brand-mark"></div>
    <p class="brand-name">Maple Cove Dental</p>
    <p class="brand-tagline">general dentistry for children</p>

    <div class="child-photo" role="img" aria-label="Photo of a smiling young child with a blue towel around the shoulders, holding a toothbrush"></div>

    <h1 class="headline">
      <span class="line-big">Healthy</span>
      <span class="line-big">Smiles</span>
      <span class="line-small">Start Early</span>
    </h1>

    <div class="phone-box">
      <span class="phone-number">555-014-3390</span>
    </div>
  </section>
</body>
</html>
```